Stonebrook Aerial Business Card

We are a new company based in Central Queensland, Australia that uses specalised drones (Velkor Sprayhawk K40) to undertake mainly agricultural operations, like spraying weeds, spraying crops, spreading seed etc. I have attached a Plinto proof of a card I was thinking along the lines of - purely a start point. The drone used in the business card MUST be a Velkor Sprayhawk K40.
I am very open to other ideas, especially fonts and layout. I don't have website etc set up yet.
The images are stock and easily interchangeable, I just ask that any background images reflect the local central Queensland area. The photo of the drone is not even complete (propellers cut off) and I need a new stock photo – I’m not sure if this is an issue, or I can pay for an image if need be. PLEASE FIND AN SPRAYHAWK K40 image - 4 sprayers, not 6.
The logo/business name is very draft and looking for further ideas, ideally incorporating drones or agriculture design elements into the design of the business name. The business name needs work on the graphic/design – it is a draft that I have included, the drone propellers (being a different colour) are DRAFT only and intended for changes. PLEASE DO NOT USE THE DRONE PORPELLER I HAVE USED AS A DRAFT. TRY TO FIND SOMETHING ELSE.. The arrow is a shape and not aligned in any way, I would also like ideas on different fonts and additional elements, like air streams, aviation elements, aviation or country western (farming like) themes and fonts etc.
Ideally looking at staying within the blue, green and yellow colours, keeping with an natural, outdoorsy, environmental feel.

Target Market(s)

Farmers, Agriculture, Local Governments, Land Managers

Industry/Entity Type

Agriculture, Drones, Aviation

Contact Information for Business Card

Agricultural Drone (Velkor Sprayhawk K40), Farming, Business Name.

Font styles to use
Sans Serif

Colors
0054AA
0677BA
7BADD7
CADEEF
E8F1F8
0094D4
00A9DD
6FCCEA
C7EBF8
E9F6FB
00AB8E
00BBA5
67D7C9
C6EFE9
E9F9F6
59FF00
82FF00
B8FF75
E3FFCB
F4FFEA

Requirements
Must have
• Velkor Sprayhawk K40 Drone
Should not have
• Tractors

```html
<!DOCTYPE html>
<html lang="en">
<head>
<meta charset="utf-8">
<title>Stonebrook Aerial Business Card</title>
<link rel="stylesheet" href="https://fonts.googleapis.com/css2?family=Poppins:wght@400;600&family=Roboto+Slab:wght@700;900&display=swap">
<style>
  :root {
    --backdrop: #1f1f21;
    --sky-top: #0677ba;
    --sky-mid: #6fccea;
    --horizon: #c7ebf8;
    --field-light: #5e9a2c;
    --field-dark: #2f6a1c;
    --drone-white: #f4f6f8;
    --drone-grey: #b9c2ca;
    --accent-yellow: #f3ef7a;
    --ink-white: #ffffff;
  }
  * { margin: 0; padding: 0; box-sizing: border-box; }
  html, body { width: 1200px; height: 900px; overflow: hidden; }
  body {
    background: var(--backdrop);
    display: flex;
    flex-direction: column;
    align-items: center;
    justify-content: center;
    gap: 40px;
    font-family: "Poppins", sans-serif;
  }
  .card {
    position: relative;
    width: 700px;
    height: 400px;
    border-radius: 22px;
    overflow: hidden;
    color: var(--ink-white);
  }
  .card-photo {
    position: absolute;
    inset: 0;
    background: linear-gradient(180deg,
      var(--sky-top) 0%,
      var(--sky-mid) 30%,
      var(--horizon) 40%,
      var(--field-light) 46%,
      var(--field-light) 62%,
      var(--field-dark) 100%);
  }
  .drone-photo {
    position: absolute;
    width: 200px;
    height: 110px;
    border-radius: 50%;
    background: radial-gradient(ellipse at center, var(--drone-white) 0%, var(--drone-grey) 55%, rgba(185, 194, 202, 0) 72%);
  }
  .brand-name {
    font-family: "Roboto Slab", serif;
    font-weight: 900;
    text-transform: uppercase;
    line-height: 1;
    white-space: nowrap;
    color: var(--ink-white);
  }
  .brand-tagline {
    font-family: "Roboto Slab", serif;
    font-weight: 700;
    font-style: italic;
    text-transform: uppercase;
    letter-spacing: 0.5px;
    white-space: nowrap;
    color: var(--ink-white);
  }

  /* front */
  .front .drone-photo { left: 470px; top: 28px; }
  .front .brand { position: absolute; left: 34px; top: 92px; }
  .front .brand-name { font-size: 54px; }
  .front .brand-name .line-two { display: block; padding-left: 70px; }
  .front .brand-tagline { font-size: 14px; margin-top: 10px; padding-left: 58px; }

  .contact { position: absolute; left: 62px; top: 254px; }
  .contact-name { font-size: 24px; font-weight: 600; color: var(--accent-yellow); line-height: 1.1; letter-spacing: 0.5px; }
  .contact-role { font-size: 16px; margin-bottom: 8px; }
  .contact-list { list-style: none; font-size: 15px; line-height: 1.45; }
  .contact-list li { display: flex; align-items: center; gap: 8px; }
  .contact-list svg { width: 15px; height: 15px; fill: none; stroke: var(--accent-yellow); stroke-width: 2; }

  .services { position: absolute; right: 42px; top: 206px; }
  .service-list { list-style: none; font-family: "Roboto Slab", serif; font-weight: 700; font-size: 19px; line-height: 1.2; color: var(--accent-yellow); }
  .service-list li:nth-child(2) { padding-left: 14px; }
  .service-list li:nth-child(3) { padding-left: 28px; }
  .address { margin-top: 20px; font-size: 14px; line-height: 1.35; }
  .address span { display: block; padding-left: 40px; }

  /* back */
  .back .drone-photo { left: 240px; top: 28px; width: 220px; height: 120px; }
  .back .brand { position: absolute; left: 200px; top: 158px; }
  .back .brand-name { font-size: 54px; }
  .back .brand-name .line-two { display: block; padding-left: 60px; }
  .back .brand-tagline { font-size: 14px; margin-top: 10px; padding-left: 70px; }
</style>
</head>
<body>

  <section class="card front">
    <div class="card-photo" role="img" aria-label="Photo of green Central Queensland farmland under a blue sky"></div>
    <div class="drone-photo" role="img" aria-label="Photo of a Velkor Sprayhawk K40 spray drone in flight"></div>
    <div class="brand">
      <h1 class="brand-name">Stonebrook<span class="line-two">Aerial</span></h1>
      <p class="brand-tagline">Servicing Central Queensland</p>
    </div>
    <div class="contact">
      <p class="contact-name">MARCUS HALE</p>
      <p class="contact-role">Managing Director</p>
      <ul class="contact-list">
        <li><svg viewBox="0 0 24 24"><path d="M5 3h4l2 5-3 2a11 11 0 0 0 6 6l2-3 5 2v4a2 2 0 0 1-2 2A17 17 0 0 1 3 5a2 2 0 0 1 2-2z"/></svg>044-987 654 321</li>
        <li><svg viewBox="0 0 24 24"><rect x="3" y="5" width="18" height="14"/><path d="M3 5l9 8 9-8"/></svg>hello@stonebrookaerial.au</li>
        <li><svg viewBox="0 0 24 24"><circle cx="12" cy="12" r="9"/><path d="M3 12h18M12 3c3 3 3 15 0 18M12 3c-3 3-3 15 0 18"/></svg>www.stonebrookaerial.au</li>
      </ul>
    </div>
    <div class="services">
      <ul class="service-list">
        <li>Spraying Weeds</li>
        <li>Spraying Crops</li>
        <li>Spreading Seeds</li>
      </ul>
      <p class="address">421, Address line goes here<span>45452 Country Name</span></p>
    </div>
  </section>

  <section class="card back">
    <div class="card-photo" role="img" aria-label="Photo of green Central Queensland paddocks and a river under a blue sky"></div>
    <div class="drone-photo" role="img" aria-label="Photo of a Velkor Sprayhawk K40 spray drone hovering"></div>
    <div class="brand">
      <h2 class="brand-name">Stonebrook<span class="line-two">Aerial</span></h2>
      <p class="brand-tagline">Servicing Central Queensland</p>
    </div>
  </section>

</body>
</html>
```